Etiketten für Honiggläser
Zielgruppe
Ich bin ein Imker und möchte meinen Honig verkaufen.
Aufgabenstellung
Ich möchte exklusive und edle Honigetiketten die auffallen. Ich habe weder ein Logo noch hat meine Imkerei einen Namen. ( Vorschläge sind aber auch willkommen ).
Auf die Vorderseite des Honigetiketts soll zu lesen sein:
- Deutscher Honig
- Art des Honigs: Blütenhonig / Waldhonig ...
- 500g
Auf der Rückseite des Honigetiketts soll zu finden sein:
- Namen und Adresse des Imkers
- freies Feld für das Mindesthaltbarkeitsdatum
Ergänzende Informationen:
- Name: Tobias Wend
- Adresse: Lindauer Gasse 47, 85399 Eggmoos ( Bayern )
Bitte in einem Format liefern, dass ich ohne Aufwände an eine Druckerei übergeben kann. Außerdem muss ich die Dateien bearbeiten können in Photoshop o.ä. um zB die Art des Honigs und die Füllmenge anpassen zu können.
Wichtig:
Die Abmessungen des Labels sollen 15,5cm - 17cm breit und 6cm hoch sein.

```html
<!DOCTYPE html>
<html lang="de">
<head>
<meta charset="utf-8">
<title>Honigetikett – Tobias Wend</title>
<link href="https://fonts.googleapis.com/css2?family=Inter:wght@300;400;600&display=swap" rel="stylesheet">
<style>
  :root {
    --page-bg: #ebebeb;
    --label-bg: #ffffff;
    --ink: #111111;
    --ink-soft: #333333;
  }
  html, body {
    margin: 0;
    padding: 0;
    width: 1200px;
    height: 960px;
    overflow: hidden;
    background: var(--page-bg);
  }
  .canvas {
    position: relative;
    width: 1200px;
    height: 960px;
  }
  .label {
    position: absolute;
    left: 80px;
    top: 285px;
    width: 1040px;
    height: 390px;
    background: var(--label-bg);
    box-shadow: 0 2px 18px rgba(0,0,0,0.06);
    overflow: hidden;
    font-family: "Inter", Helvetica, Arial, sans-serif;
    color: var(--ink);
  }
  .label__badge {
    position: absolute;
    left: 0;
    top: 0;
    width: 520px;
    height: 390px;
  }
  .label__badge svg {
    position: absolute;
    inset: 0;
  }
  .badge__origin {
    position: absolute;
    left: 72px;
    top: 100px;
    font-size: 15px;
    font-weight: 400;
    letter-spacing: 2px;
    text-transform: uppercase;
  }
  .badge__mark {
    position: absolute;
    left: 70px;
    top: 136px;
    display: flex;
    align-items: center;
    gap: 18px;
  }
  .badge__name {
    font-size: 64px;
    font-weight: 600;
    letter-spacing: -1px;
    line-height: 1;
  }
  .badge__dot {
    width: 14px;
    height: 14px;
    border-radius: 50%;
    background: var(--ink);
  }
  .badge__variety {
    position: absolute;
    left: 72px;
    top: 214px;
    font-size: 30px;
    font-weight: 300;
    letter-spacing: 0.5px;
    line-height: 1;
  }
  .badge__weight {
    position: absolute;
    left: 72px;
    top: 262px;
    font-size: 17px;
    font-weight: 400;
    letter-spacing: 1px;
  }
  .label__back {
    position: absolute;
    right: 70px;
    top: 60px;
    width: 300px;
    text-align: right;
    font-size: 17px;
    font-weight: 300;
    line-height: 1.3;
    color: var(--ink-soft);
  }
  .label__address {
    font-style: normal;
  }
  .label__address p { margin: 0; }
  .label__bestbefore {
    margin-top: 150px;
    font-size: 14px;
    font-weight: 300;
  }
  .bestbefore__field {
    display: block;
    margin-top: 26px;
    margin-left: auto;
    width: 220px;
    border-bottom: 1px solid var(--ink);
  }
</style>
</head>
<body>
<div class="canvas">
  <section class="label">
    <div class="label__badge">
      <svg width="520" height="390" viewBox="0 0 520 390">
        <polyline points="0,70 330,70 430,195 330,320 0,320"
                  fill="none" stroke="var(--ink)" stroke-width="2"/>
      </svg>
      <div class="badge__origin">Deutscher Honig</div>
      <div class="badge__mark">
        <span class="badge__name">Wend</span>
        <span class="badge__dot"></span>
      </div>
      <div class="badge__variety">Blütenhonig</div>
      <div class="badge__weight">500g</div>
    </div>
    <div class="label__back">
      <address class="label__address">
        <p>Tobias Wend</p>
        <p>Lindauer Gasse 47</p>
        <p>85399 Eggmoos</p>
      </address>
      <div class="label__bestbefore">
        Mindestens haltbar bis:
        <span class="bestbefore__field"></span>
      </div>
    </div>
  </section>
</div>
</body>
</html>
```